App Design for quiz app (casual gaming app)

We need an design & logo for our quiz app. Its a simple quiz app, where you pick up a category, answer three questions out of this category. After this an opponent is assigned to your game, and has to answer the same three questions. After this first round is finished, it's the opponents turn to choose a new category and answer three questions out of this category. Now it's your turn to answer the same three questions. With this done, the 2nd round is finished. One game has seven rounds.
Please find attached the balsamiq project. For all of you, do not have balsamiq, please find also the mockups as pdf.
Final delivery should be psd files
Target Market(s)
Casual Games

```html
<!DOCTYPE html>
<html lang="en">
<head>
<meta charset="utf-8">
<title>Quiz – Science Question</title>
<link href="https://fonts.googleapis.com/css2?family=Carlito:wght@400;700&family=Roboto:wght@300;400&display=swap" rel="stylesheet">
<style>
  :root {
    --bar-dark: #3b4550;
    --sunflower: #fec452;
    --caramel: #c48c4a;
    --coral: #fd8373;
    --white: #ffffff;
    --cyan: #1fb5d8;
  }
  * { box-sizing: border-box; margin: 0; padding: 0; }
  html, body { width: 674px; height: 1200px; overflow: hidden; background: var(--white); }
  .screen { position: relative; width: 674px; height: 1200px; font-family: "Carlito", sans-serif; color: var(--white); overflow: hidden; }

  .status-bar { position: absolute; top: 0; left: 0; width: 674px; height: 40px; font-family: "Roboto", sans-serif; font-weight: 300; font-size: 22px; }
  .status-carrier { position: absolute; left: 12px; top: 6px; display: flex; align-items: center; gap: 8px; }
  .status-time { position: absolute; left: 0; right: 0; top: 5px; text-align: center; }
  .status-battery { position: absolute; right: 14px; top: 6px; display: flex; align-items: center; gap: 6px; }

  .nav-bar { position: absolute; top: 0; left: 0; width: 674px; height: 112px; background: var(--bar-dark); }
  .nav-back { position: absolute; left: 28px; top: 58px; }
  .nav-title { position: absolute; left: 0; right: 0; top: 59px; text-align: center; font-weight: 700; font-size: 33px; line-height: 42px; }

  .question-panel { position: absolute; top: 112px; left: 0; width: 674px; height: 298px; background: var(--sunflower); }
  .question-badge { position: absolute; left: 223px; top: 22px; width: 247px; height: 56px; border-radius: 28px; background: var(--caramel); font-weight: 700; font-size: 34px; text-align: center; line-height: 56px; word-spacing: 14px; }
  .question-text { position: absolute; left: 10px; right: 10px; top: 104px; text-align: center; font-weight: 700; font-size: 34px; line-height: 43px; }

  .answers { position: absolute; left: 30px; top: 490px; width: 607px; list-style: none; }
  .answer { height: 81px; margin-bottom: 27px; border: 4px solid var(--sunflower); border-radius: 41px; color: var(--sunflower); font-weight: 700; font-size: 35px; display: flex; align-items: center; justify-content: center; }
  .answer--selected { background: var(--sunflower); color: var(--white); }

  .like { position: absolute; left: 595px; top: 986px; }

  .score-panel { position: absolute; top: 1058px; left: 0; width: 674px; height: 142px; background: var(--coral); }
  .timer { position: absolute; left: 34px; top: 52px; font-weight: 700; font-size: 40px; line-height: 49px; }
  .round { position: absolute; left: 227px; width: 240px; top: 32px; text-align: center; }
  .round-number { display: block; font-weight: 700; font-size: 54px; line-height: 46px; }
  .round-label { display: block; font-size: 43px; line-height: 40px; }
  .points { position: absolute; left: 550px; width: 100px; top: 45px; text-align: center; }
  .points-value { display: block; font-size: 43px; line-height: 40px; }
  .points-label { display: block; font-size: 23px; line-height: 28px; }
</style>
</head>
<body>
<main class="screen">
  <header class="nav-bar">
    <div class="status-bar">
      <div class="status-carrier">
        <svg width="72" height="12" viewBox="0 0 72 12" aria-hidden="true">
          <circle cx="6" cy="6" r="5" fill="#fff"/><circle cx="20" cy="6" r="5" fill="#fff"/>
          <circle cx="34" cy="6" r="4.5" fill="none" stroke="#fff" stroke-width="1"/>
          <circle cx="48" cy="6" r="4.5" fill="none" stroke="#fff" stroke-width="1"/>
          <circle cx="62" cy="6" r="4.5" fill="none" stroke="#fff" stroke-width="1"/>
        </svg>
        <span>NX</span>
        <svg width="22" height="16" viewBox="0 0 22 16" aria-hidden="true">
          <path d="M1 5a14 14 0 0 1 20 0M4.5 8.5a9 9 0 0 1 13 0M8 12a4 4 0 0 1 6 0" fill="none" stroke="#fff" stroke-width="2.4" stroke-linecap="round"/>
        </svg>
      </div>
      <div class="status-time">12:53 pm</div>
      <div class="status-battery">
        <span>31%</span>
        <svg width="52" height="20" viewBox="0 0 52 20" aria-hidden="true">
          <rect x="1" y="1" width="46" height="18" rx="3" fill="none" stroke="#fff" stroke-width="1.5"/>
          <rect x="3.5" y="3.5" width="13" height="13" fill="#fff"/>
          <rect x="48.5" y="7" width="2.5" height="6" fill="#fff"/>
        </svg>
      </div>
    </div>
    <svg class="nav-back" width="26" height="44" viewBox="0 0 26 44" aria-label="Back">
      <path d="M23 3 5 22l18 19" fill="none" stroke="var(--cyan)" stroke-width="4" stroke-linecap="round"/>
    </svg>
    <h1 class="nav-title">Science</h1>
  </header>

  <section class="question-panel">
    <div class="question-badge">Question 3</div>
    <p class="question-text">Brass gets discoloured<br>in air because of the presence of which<br>of the following gases in air ?</p>
  </section>

  <ul class="answers">
    <li class="answer">Oxygen</li>
    <li class="answer answer--selected">Hydrogen sulphide</li>
    <li class="answer">Carbon dioxide</li>
    <li class="answer">Nitrogen</li>
  </ul>

  <svg class="like" width="44" height="38" viewBox="0 0 44 38" aria-label="Favourite">
    <path d="M22 37 4 20C-1 15 0 5 7 2c5-2 11 0 15 5 4-5 10-7 15-5 7 3 8 13 3 18Z" fill="var(--coral)"/>
  </svg>

  <footer class="score-panel">
    <div class="timer">02:12</div>
    <div class="round">
      <span class="round-number">4</span>
      <span class="round-label">Round</span>
    </div>
    <div class="points">
      <span class="points-value">12</span>
      <span class="points-label">points</span>
    </div>
  </footer>
</main>
</body>
</html>
```